BOOK: The Backer Marketplace

The book will be about raising money online through crowdfunding. The author is an authority in the field.

Title: The Backer Marketplace
Subtitle: Gather Funds Digitally for a T.R.U.F.L.E. (Talent, Rollout, Undertaking, Fund, Launch, or Endeavor)
Author: Marlon Quibbet

One idea we have for the book cover design is to create an element of surprise or feeling of conflict and yet overall sense of harmony for the viewer.

On the one hand the book cover design should show wealth, money, elegance: This might be accomplished through a color scheme of gold on white. (See attached sample book cover we like that might inspire you).

On the other hand the book cover design should also convey the power of the crowds which defy an air of exclusivity normally associated with wealth and elegance This might be accomplished through the use of geometric patterns that represent waves or fluidity or tapestry or similar concepts.

The design should convey high touch and organic growth as crowdfunding is closely associated with social media and crowdsourcing or shared economies. The cover should also depict high tech and innovation as crowdfunding is one of the financial technologies now making waves in the financial and business world as it optimizes the internet and online automation.

Design can also have tactile feel to it just like the sample, to compensate for the 2-tone color theme if that is chosen.

If you have other ideas how this can be best depicted using other color schemes or design concepts, please feel free to do so. Who knows we might like your concept better :-)

Target Market(s)

All people who care about crowdfunding, young and old, male or female. Global citizens. But leaning towards 35-80 years old, professional, new and veteran investors.

Industry/Entity Type

Finance

Font styles to use
Other font styles liked:
• Calibri

Colors
fbee3d
ffffff

Requirements
Must have
• see project description
Nice to have
• see project description
Should not have
• Common designs usually used or concepts already used by other Crowdfunding Books. We want this one to stand out from the rest, be distinct, remarkable, elegant and yet low key, simple and thought-provoking.
• NOTE: DO NOT USE WHITE COLOR FOR THE TEXT

```html
<!DOCTYPE html>
<html lang="en">
<head>
<meta charset="utf-8">
<title>The Backer Marketplace — Marlon Quibbet</title>
<link rel="stylesheet" href="https://fonts.googleapis.com/css2?family=Bebas+Neue&family=Dancing+Script:wght@700&family=Open+Sans:wght@400;600&display=swap">
<style>
  :root {
    --paper: #ffffff;
    --ink: #2b2b2b;
    --ink-soft: #4a4a4a;
    --steel-light: #b0b0b0;
    --steel-mid: #808080;
    --steel-dark: #555555;
    --gold: #e3a92b;
    --gold-bright: #fbee3d;
    --note-green: #c5cbaa;
    --note-shadow: #8f9577;
  }
  * { margin: 0; padding: 0; box-sizing: border-box; }
  html, body { width: 826px; height: 1200px; overflow: hidden; background: var(--paper); }
  .cover {
    position: relative;
    width: 826px;
    height: 1200px;
    background: var(--paper);
    overflow: hidden;
  }
  .title-lead {
    position: absolute;
    left: 30px;
    top: 0;
    font-family: "Dancing Script", cursive;
    font-size: 64px;
    color: var(--ink);
    line-height: 1;
  }
  .title-main {
    position: absolute;
    left: 0;
    width: 100%;
    text-align: center;
    font-family: "Bebas Neue", sans-serif;
    font-weight: 400;
    line-height: 1;
    background: linear-gradient(180deg, var(--steel-light) 0%, var(--steel-mid) 55%, var(--steel-dark) 100%);
    -webkit-background-clip: text;
    background-clip: text;
    color: transparent;
    filter: drop-shadow(2px 3px 1px rgba(0,0,0,0.25));
  }
  .title-main--first { top: 48px; font-size: 180px; letter-spacing: 10px; }
  .title-main--second { top: 212px; font-size: 150px; letter-spacing: 4px; }
  .subtitle {
    position: absolute;
    left: 0;
    top: 368px;
    width: 100%;
    text-align: center;
    font-family: "Open Sans", sans-serif;
    font-weight: 400;
    color: var(--ink-soft);
    font-size: 23px;
    line-height: 34px;
  }
  .subtitle .acronym { font-weight: 400; }
  .artwork {
    position: absolute;
    left: 20px;
    top: 452px;
    width: 786px;
    height: 580px;
    background:
      radial-gradient(circle at 50% 50%, rgba(251,238,61,0.35) 0, rgba(251,238,61,0) 6%),
      radial-gradient(ellipse 50% 50% at 50% 50%, var(--paper) 0%, var(--paper) 30%, var(--note-green) 48%, var(--note-shadow) 62%, var(--note-green) 76%, var(--paper) 100%);
  }
  .rule {
    position: absolute;
    left: 40px;
    width: 746px;
    height: 5px;
    background: linear-gradient(90deg, var(--gold), var(--gold-bright), var(--gold));
  }
  .rule--top { top: 1046px; }
  .rule--bottom { top: 1186px; }
  .author {
    position: absolute;
    left: 0;
    top: 1064px;
    width: 100%;
    text-align: center;
    font-family: "Bebas Neue", sans-serif;
    font-weight: 400;
    font-size: 116px;
    letter-spacing: 9px;
    line-height: 1;
    color: var(--ink);
  }
</style>
</head>
<body>
  <main class="cover">
    <header class="title-block">
      <span class="title-lead">The</span>
      <h1>
        <span class="title-main title-main--first">BACKER</span>
        <span class="title-main title-main--second">MARKETPLACE</span>
      </h1>
      <p class="subtitle">
        Gather Funds Digitally for a <span class="acronym">T.R.U.F.L.E.</span><br>
        (Talent, Rollout, Undertaking, Fund, Launch, or Endeavor)
      </p>
    </header>

    <div class="artwork" role="img" aria-label="Stacks of banknotes arranged in a ring like the hours of a clock face on white, with gold clock hands at the centre"></div>

    <div class="rule rule--top"></div>
    <p class="author">MARLON QUIBBET</p>
    <div class="rule rule--bottom"></div>
  </main>
</body>
</html>
```